Brightmere Business Card Redesign & Logo Update

We need to update our business cards to something more modern and fresh. Brightmere can provide the current color schemes and old design examples, but welcome creativity in helping us with this redesign. PLEASE NOTE that we no longer utilize the "tree" and/or "leaf" imagery in our branding. If able would apprecaite an update on the quality of our "words only" logo in Ai. / PNG formats too.

Target Market(s)

Investors, landowners, corporate partners, contractors

Industry/Entity Type

Environmental Restoration & Conservation

Contact Information for Business Card

Logo, persons name, title, mailing address, phone and email, website url

Font styles to use
Other font styles liked:
• Merriweather

Requirements
Nice to have
• Logo, persons name, title, mailing address, phone and email, website url, but open to ideams
Should not have
• No all back backgrounds

```html
<!DOCTYPE html>
<html lang="en">
<head>
<meta charset="utf-8">
<title>Brightmere Business Card</title>
<link href="https://fonts.googleapis.com/css2?family=Oswald:wght@500;600&family=Arimo:wght@400&display=swap" rel="stylesheet">
<style>
  :root {
    --bg: #d9d9db;
    --paper: #ffffff;
    --charcoal: #2b2b2e;
    --charcoal-deep: #1f1f21;
    --orange: #e07b10;
    --green: #1b7f3f;
    --ink: #1d1d1d;
    --grey: #777a7e;
    --light: #f2f2f2;
  }
  html, body {
    margin: 0;
    width: 1200px;
    height: 793px;
    overflow: hidden;
    background: var(--bg);
  }
  .canvas {
    position: relative;
    width: 1200px;
    height: 793px;
    display: flex;
    align-items: center;
    justify-content: center;
    gap: 40px;
  }
  .card {
    position: relative;
    width: 540px;
    height: 309px;
    border-radius: 16px;
    overflow: hidden;
    box-shadow: 0 0 0 2px var(--green), 0 10px 24px rgba(0,0,0,.18);
  }
  .card-front { background: var(--paper); }
  .card-front .swoosh {
    position: absolute;
    inset: 0;
    width: 100%;
    height: 100%;
  }
  .brand {
    position: absolute;
    left: 36px;
    top: 96px;
  }
  .brand-name {
    font-family: "Oswald", sans-serif;
    font-weight: 600;
    font-size: 44px;
    line-height: 1;
    letter-spacing: 1px;
    color: var(--green);
    text-transform: uppercase;
  }
  .brand-tagline {
    font-family: "Oswald", sans-serif;
    font-weight: 500;
    font-size: 11.5px;
    letter-spacing: .6px;
    color: var(--ink);
    text-transform: uppercase;
    margin-top: 3px;
  }
  .person {
    position: absolute;
    left: 38px;
    top: 180px;
  }
  .person-name {
    font-family: "Oswald", sans-serif;
    font-weight: 500;
    font-size: 26px;
    line-height: 1;
    text-transform: uppercase;
  }
  .person-name .first { color: var(--orange); }
  .person-name .last { color: var(--green); }
  .person-title {
    font-family: "Arimo", sans-serif;
    font-size: 13px;
    color: var(--grey);
    margin-top: 5px;
  }
  .contact {
    position: absolute;
    right: 24px;
    top: 112px;
    text-align: right;
    font-family: "Arimo", sans-serif;
    font-style: normal;
    font-size: 12px;
    line-height: 1.45;
    color: var(--light);
  }
  .contact-row {
    display: flex;
    justify-content: flex-end;
    align-items: center;
    gap: 7px;
  }
  .contact-row svg { width: 11px; height: 11px; flex: none; }
  .contact-web { color: var(--orange); margin-top: 6px; }
  .card-back { background: var(--charcoal); }
  .card-back .pattern-field {
    position: absolute;
    inset: 0;
    background: radial-gradient(ellipse at 50% 50%, #333336 0%, var(--charcoal) 55%, var(--charcoal-deep) 100%);
  }
  .card-back .brand {
    left: 0;
    right: 0;
    top: 122px;
    text-align: center;
  }
  .card-back .brand-name { font-size: 42px; }
  .card-back .brand-tagline { color: var(--light); font-size: 11px; }
</style>
</head>
<body>
<main class="canvas">
  <section class="card card-front" aria-label="Business card front">
    <svg class="swoosh" viewBox="0 0 540 309" preserveAspectRatio="none" aria-hidden="true">
      <defs>
        <path id="wave" d="M560 24 C460 28 400 40 370 70 C330 112 312 190 272 232 C232 274 190 290 -20 296 L-20 330 L560 330 Z"/>
      </defs>
      <use href="#wave" transform="translate(-16 -14)" fill="var(--orange)"/>
      <use href="#wave" transform="translate(-11 -10)" fill="var(--paper)"/>
      <use href="#wave" transform="translate(-9 -8)" fill="var(--green)"/>
      <use href="#wave" transform="translate(-3 -3)" fill="var(--paper)"/>
      <use href="#wave" fill="var(--charcoal)"/>
    </svg>
    <div class="brand">
      <div class="brand-name">Brightmere</div>
      <div class="brand-tagline">Environmental Credit Company</div>
    </div>
    <div class="person">
      <div class="person-name"><span class="first">Daniel</span> <span class="last">Mercer</span></div>
      <div class="person-title">Managing Director</div>
    </div>
    <address class="contact">
      <div class="contact-row">4120 Harbor View Road</div>
      <div class="contact-row">Juneau, Alaska 99801</div>
      <div class="contact-row">907-555-0142
        <svg viewBox="0 0 12 12"><path d="M2.5 1 L4.5 1 L5.2 3.5 L4 4.6 C4.7 6 6 7.3 7.4 8 L8.5 6.8 L11 7.5 L11 9.5 C11 10.3 10.3 11 9.5 11 C5 11 1 7 1 2.5 C1 1.7 1.7 1 2.5 1 Z" fill="var(--orange)"/></svg>
      </div>
      <div class="contact-row">907-555-0187
        <svg viewBox="0 0 12 12"><rect x="3" y="0.8" width="6" height="10.4" rx="1" fill="none" stroke="var(--orange)" stroke-width="1.4"/></svg>
      </div>
      <div class="contact-row">info@brightmere.com
        <svg viewBox="0 0 12 12"><rect x="0.8" y="2.5" width="10.4" height="7" fill="var(--orange)"/><path d="M1 3 L6 6.6 L11 3" fill="none" stroke="var(--charcoal)" stroke-width="1"/></svg>
      </div>
      <div class="contact-row contact-web">www.brightmere.com</div>
    </address>
  </section>

  <section class="card card-back" aria-label="Business card back">
    <div class="pattern-field" role="img" aria-label="Tone-on-tone embossed repeat of the company name across the dark card"></div>
    <div class="brand">
      <div class="brand-name">Brightmere</div>
      <div class="brand-tagline">Environmental Credit Company</div>
    </div>
  </section>
</main>
</body>
</html>
```